strength and conditioning business focused on helping people move more efficiently

I need a business card designed for a Philadelphia based company called Trk Vlt Motion (pronounced Track Volt). We offer fitness professional services with the idea of helping people feel better and move optimally. We do this by designing and walking through individualized programs as well as minor soft tissue work. Our perfect client would be athletes but we will be marketing to parents who have children that are active They remember their former athletic days and want to get as close as possible back to that feeling. Attached will be the official logo and logo formats. I would love for the design to communicate trustworthy and creative. I would also love for the design to be square with rounded edges.

Target Market(s)

Parents of athletic children
former athletes
athletes

Industry/Entity Type

Fitness

Contact Information for Business Card

Business: Trk Vlt Performance
Name: Coach Garrett Ellison
Position: Strength and Conditioning Coach / Certified Personal Trainer
Contact: coach.ell@trkvlt-example.com
Text: (555)204-7719

Font styles to use
Serif
Sans Serif

Colors
fbee38
fbee3e
0255a3
3176b5
ffffff

Requirements
Must have
• use of logo
Nice to have
• Square design
rounded edges

```html
<!DOCTYPE html>
<html lang="en">
<head>
<meta charset="utf-8">
<title>Trk Vlt Motion — Business Card</title>
<link rel="stylesheet" href="https://fonts.googleapis.com/css2?family=Arimo:wght@400;700&display=swap">
<style>
  :root {
    --backdrop: #6b6b6b;
    --navy: #0b2d72;
    --gold: #f7c51e;
    --white: #ffffff;
    --ink: #111111;
    --radius: 32px;
  }
  * { box-sizing: border-box; margin: 0; padding: 0; }
  html, body {
    width: 1200px;
    height: 802px;
    overflow: hidden;
    background: var(--backdrop);
    font-family: "Arimo", Arial, sans-serif;
  }
  .card {
    position: absolute;
    top: 175px;
    width: 462px;
    height: 458px;
    border-radius: var(--radius);
    box-shadow: 4px 6px 10px rgba(0,0,0,0.35);
  }
  /* Front side */
  .card--front {
    left: 123px;
    background: var(--navy);
    display: flex;
    flex-direction: column;
    align-items: center;
    justify-content: center;
    gap: 26px;
  }
  .front-mark {
    width: 96px;
    height: 96px;
    border-radius: 50%;
    border: 10px solid var(--gold);
  }
  .front-name {
    color: var(--white);
    font-weight: 700;
    font-size: 78px;
    line-height: 0.98;
    text-align: center;
    letter-spacing: 1px;
  }
  /* Back side */
  .card--back {
    left: 617px;
    background: var(--white);
    text-align: center;
  }
  .back-brand {
    position: absolute;
    top: 62px;
    left: 0;
    right: 0;
    display: flex;
    align-items: center;
    justify-content: center;
    gap: 12px;
  }
  .back-mark {
    width: 44px;
    height: 44px;
    border-radius: 50%;
    border: 5px solid var(--gold);
  }
  .back-name {
    color: var(--navy);
    font-weight: 700;
    font-size: 40px;
  }
  .person {
    position: absolute;
    top: 190px;
    left: 0;
    right: 0;
  }
  .person-name {
    color: var(--navy);
    font-weight: 700;
    font-size: 28px;
    margin-bottom: 6px;
  }
  .person-role {
    color: var(--ink);
    font-size: 17px;
    line-height: 1.45;
  }
  .contact-icons {
    position: absolute;
    top: 307px;
    left: 0;
    right: 0;
    display: flex;
    justify-content: center;
    gap: 10px;
  }
  .contact-icons svg { width: 34px; height: 34px; }
  .contact {
    position: absolute;
    top: 360px;
    left: 0;
    right: 0;
    color: var(--ink);
    font-size: 20px;
    line-height: 1.75;
  }
</style>
</head>
<body>
  <section class="card card--front" aria-label="Card front">
    <div class="front-mark"></div>
    <div class="front-name">Trk Vlt<br>Motion</div>
  </section>

  <section class="card card--back" aria-label="Card back">
    <div class="back-brand">
      <div class="back-mark"></div>
      <div class="back-name">Trk Vlt Motion</div>
    </div>

    <div class="person">
      <h1 class="person-name">Coach Garrett Ellison</h1>
      <p class="person-role">Strength and Conditioning Coach<br>Certified Personal Trainer</p>
    </div>

    <div class="contact-icons">
      <svg viewBox="0 0 34 34" aria-label="Phone">
        <circle cx="17" cy="17" r="15" fill="var(--white)" stroke="var(--gold)" stroke-width="2.5"/>
        <path d="M11.5 9.5 l3.5 -0.5 l1.6 4 l-2.2 1.6 q1.6 3.4 4.9 4.9 l1.6 -2.2 l4 1.6 l-0.5 3.5 q-8.5 0.5 -12.9 -12.9z" fill="var(--navy)"/>
      </svg>
      <svg viewBox="0 0 34 34" aria-label="Email">
        <circle cx="17" cy="17" r="15" fill="var(--white)" stroke="var(--gold)" stroke-width="2.5"/>
        <rect x="9" y="11.5" width="16" height="11" fill="none" stroke="var(--navy)" stroke-width="1.8"/>
        <path d="M9 11.5 L17 18 L25 11.5" fill="none" stroke="var(--navy)" stroke-width="1.8"/>
      </svg>
    </div>

    <div class="contact">
      <p class="contact-phone">(555)204-7719</p>
      <p class="contact-email">coach.ell@trkvlt-example.com</p>
    </div>
  </section>
</body>
</html>
```